Buchcover-Design für psychologischen Ratgeber Morgens voller Mut!
Zielgruppe
Veröffentlichung psychologischer Ratgeber. Zielgruppe sind Erwachsene.
Aufgabenstellung
keine besondere Vorgaben, ein eyecatching-Cover wäre super. Der Titel des Buches lautet: Morgens voller Mut! Der Untertitel lautet: Heitere Seelenkunde für stille Kraft und Zuversicht
Autoren: Dr. Hanna Wiesmoor-Kalbach, Dr. Lukas Kalbach
Vielleicht macht es Sinn, einen Button mit: 199 Praxistipps auf dem Cover anzuführen.
Das Buch wird als Softcover und Ebook auf lesewelt veröffentlicht. Das Format ist 6 mal 9 Zoll und hat 425 Seiten.

```html
<!DOCTYPE html>
<html lang="de">
<head>
<meta charset="utf-8">
<title>Morgens voller Mut! – Buchcover</title>
<link rel="stylesheet" href="https://fonts.googleapis.com/css2?family=Fira+Sans+Condensed:wght@600;700&family=Fira+Sans+Extra+Condensed:wght@400;500&family=Fira+Sans:wght@400&display=swap">
<style>
  :root {
    --backdrop: #e9eaec;
    --backdrop-edge: #dcdee1;
    --board: #f7f7f7;
    --title-orange: #e8601f;
    --accent-blue: #1e73b9;
    --navy: #14305a;
    --plate: #000000;
    --plate-text: #ffffff;
  }
  * { margin: 0; padding: 0; box-sizing: border-box; }
  html, body { width: 800px; height: 1200px; overflow: hidden; background: var(--backdrop); }
  .cover {
    position: relative;
    width: 800px;
    height: 1200px;
    overflow: hidden;
    background: var(--backdrop);
  }
  .group-photo {
    position: absolute;
    inset: 0;
    background:
      radial-gradient(ellipse 46% 30% at 50% 30%, #c9a78f 0%, rgba(201,167,143,0) 70%),
      radial-gradient(ellipse 22% 45% at 14% 82%, #2c3d63 0%, rgba(44,61,99,0) 75%),
      radial-gradient(ellipse 18% 45% at 86% 72%, #4f83c1 0%, rgba(79,131,193,0) 75%),
      linear-gradient(180deg, var(--backdrop) 0%, var(--backdrop-edge) 100%);
  }
  .board {
    position: absolute;
    left: 166px;
    top: 432px;
    width: 504px;
    height: 800px;
    background: var(--board);
    transform: skewX(1.2deg);
  }
  .authors {
    position: absolute;
    top: 26px;
    left: 0;
    width: 800px;
    text-align: center;
    font-family: "Fira Sans Condensed", sans-serif;
    font-weight: 700;
    font-size: 26px;
    letter-spacing: 0.2px;
    color: var(--accent-blue);
  }
  .title {
    position: absolute;
    left: 186px;
    top: 508px;
    width: 456px;
    font-family: "Fira Sans Extra Condensed", sans-serif;
    font-weight: 500;
    font-size: 100px;
    line-height: 1.12;
    letter-spacing: -2px;
    color: var(--title-orange);
  }
  .title span { display: block; white-space: nowrap; }
  .subtitle {
    position: absolute;
    right: 185px;
    top: 786px;
    text-align: right;
  }
  .subtitle-kicker {
    font-family: "Fira Sans Condensed", sans-serif;
    font-weight: 700;
    font-size: 44px;
    line-height: 1.18;
    letter-spacing: 5px;
    margin-right: -5px;
    color: var(--accent-blue);
    text-transform: uppercase;
  }
  .subtitle-line {
    font-family: "Fira Sans Condensed", sans-serif;
    font-weight: 600;
    font-size: 40px;
    line-height: 1.2;
    letter-spacing: -0.5px;
    color: var(--navy);
  }
  .publisher {
    position: absolute;
    left: 315px;
    top: 1125px;
    width: 173px;
    height: 75px;
    background: var(--plate);
    display: flex;
    align-items: center;
    justify-content: center;
    font-family: "Fira Sans", sans-serif;
    font-weight: 400;
    font-size: 18px;
    color: var(--plate-text);
  }
</style>
</head>
<body>
  <main class="cover">
    <div class="group-photo" role="img" aria-label="Fotografie: fünf lächelnde junge Erwachsene stehen vor hellgrauem Hintergrund hinter einer großen weißen Tafel"></div>
    <div class="board"></div>

    <p class="authors">Dr. Hanna Wiesmoor-Kalbach &amp; Dr. Lukas Kalbach</p>

    <h1 class="title">
      <span>Morgens</span>
      <span>voller Mut!</span>
    </h1>

    <div class="subtitle">
      <p class="subtitle-kicker">Heitere</p>
      <p class="subtitle-kicker">Seelenkunde</p>
      <p class="subtitle-line">für stille Kraft</p>
      <p class="subtitle-line">und Zuversicht</p>
    </div>

    <div class="publisher">Verlag Lichtblick</div>
  </main>
</body>
</html>
```